Business Card Design Project

Corvexa logo will be provided after
Front

Ned Marrowick- Construction Manager

Ph: (61) 07 53182079
nmarrowick@corvexa-example.com.au
PO Box 83 Kelvorin 4619

Back
Corvexa
EPCM

Oil - Gas - Mining

Industry/Entity Type

Business

Font styles to use
Sans Serif

Colors
faa54b

Requirements
Must have
• White Back Ground

```html
<!DOCTYPE html>
<html lang="en">
<head>
<meta charset="utf-8">
<title>Corvexa Business Card</title>
<link rel="stylesheet" href="https://fonts.googleapis.com/css2?family=Source+Sans+3:wght@400;700&display=swap">
<style>
  :root {
    --stage: #2a211c;
    --paper: #ffffff;
    --ink: #141414;
    --orange: #f0931f;
    --grey-text: #3a3a3a;
    --rule: #c9c9c9;
    --night: #000000;
  }
  * { box-sizing: border-box; margin: 0; padding: 0; }
  html, body {
    width: 1136px; height: 1200px; overflow: hidden;
    background: var(--stage);
    font-family: "Source Sans 3", sans-serif;
  }
  .card { position: absolute; }
  .card--front { left: 41px; top: 104px; width: 846px; height: 483px; background: var(--paper); }
  .card--back { left: 248px; top: 613px; width: 849px; height: 484px; background: var(--night); }

  .wordmark {
    position: absolute; left: 0; right: 0;
    text-align: center; font-weight: 700;
    font-size: 84px; letter-spacing: 6px; line-height: 1;
  }
  .card--front .wordmark { top: 92px; color: var(--ink); }
  .card--back .wordmark { top: 178px; color: var(--paper); }

  .rule { position: absolute; left: 0; right: 0; height: 3px; background: var(--ink); }
  .rule--top { top: 245px; }
  .rule--bottom { top: 306px; }
  .name-band {
    position: absolute; left: 0; right: 0; top: 253px; height: 48px;
    background: var(--orange); color: var(--paper);
    display: flex; align-items: center; justify-content: center;
    font-size: 21px;
  }
  .name-band .person { font-weight: 700; font-size: 26px; margin-right: 6px; }

  .address {
    position: absolute; right: 493px; top: 366px;
    text-align: right; color: var(--grey-text);
    font-size: 21px; line-height: 30px;
  }
  .divider { position: absolute; left: 371px; top: 358px; width: 1px; height: 78px; background: var(--rule); }
  .contacts { position: absolute; left: 384px; top: 354px; list-style: none; color: var(--grey-text); font-size: 21px; }
  .contacts li { display: flex; align-items: center; height: 29px; }
  .contacts svg { width: 18px; height: 18px; margin-right: 8px; flex: none; }

  .web {
    position: absolute; left: 0; right: 0; top: 332px;
    text-align: center; color: var(--paper);
    font-size: 26px; letter-spacing: 4px;
  }
</style>
</head>
<body>
  <section class="card card--front" aria-label="Card front">
    <div class="wordmark">CORVEXA</div>
    <div class="rule rule--top"></div>
    <div class="name-band"><span class="person">Ned Marrowick,</span> Construction Manager</div>
    <div class="rule rule--bottom"></div>
    <div class="address">PO Box<br>83 Kelvorin 4619</div>
    <div class="divider"></div>
    <ul class="contacts">
      <li>
        <svg viewBox="0 0 20 20" aria-hidden="true"><circle cx="10" cy="10" r="8.5" fill="none" stroke="var(--orange)" stroke-width="1.5"/><path d="M7 6c-1 2 1 7 5 8l1.5-1.5-2-1.5-1 .8c-1-.5-2-2-2.3-3l.8-.8L7.8 5.5z" fill="var(--orange)"/></svg>
        (61) 07 53182079
      </li>
      <li>
        <svg viewBox="0 0 20 20" aria-hidden="true"><rect x="2" y="5" width="16" height="11" rx="1" fill="var(--orange)"/><path d="M2.5 5.5 10 11l7.5-5.5" fill="none" stroke="#fff" stroke-width="1.4"/></svg>
        nmarrowick@corvexa-example.com.au
      </li>
      <li>
        <svg viewBox="0 0 20 20" aria-hidden="true"><g fill="none" stroke="var(--orange)" stroke-width="1.3"><circle cx="10" cy="10" r="8"/><ellipse cx="10" cy="10" rx="3.5" ry="8"/><path d="M2 10h16M3.5 6h13M3.5 14h13"/></g></svg>
        www.corvexa-example.com.au
      </li>
    </ul>
  </section>

  <section class="card card--back" aria-label="Card back">
    <div class="wordmark">CORVEXA</div>
    <div class="web">www.corvexa-example.com.au</div>
  </section>
</body>
</html>
```